Thank you for exploring whether you are interested in creating a book cover for The Insight Lantern!

The cover should look professional yet appeal to a person who is open to approaching life more deeply.

The logo that I've uploaded is something that you are welcome to use in your book cover design but is not required to be the primary graphic.

The following is a description of The Insight Lantern and its purpose.
RADICAL CLARITY IS POSSIBLE

Are you tired of hitting up against your limitations? Do you wish you could be more effective in everything you do? What would it be like if you could walk confidently into any situation and automatically comprehend it, organize your thoughts, and respond creatively? This kind of radical clarity is not only possible, it’s right in front of you—and The Insight Lantern: Notice Every Signal. Hold Bold Dialogues. Build the Path You Choose. shows you the pathway to get there!

In the book, Dr. Gavin Terlecki draws on over 30 years of experience with executive coaching and leadership development to deliver priceless wisdom about how to see clearly in today’s complex and uncertain world. Using his Insight Lantern, you’ll discover where you’re stuck and why, find your authentic direction, and learn to engage creatively with life so you can start getting what you really want.

A TRANSFORMATIONAL TOOL

The Insight Lantern is a cutting-edge leadership development tool that supports you to activate your maximum potential, both personally and professionally. It’s based on the idea that there are four fundamental building blocks to reality: Intentions, Actions, Facts, and Stories. Understanding the differences between these dimensions of your experience and learning how they work together is the key to forging a clear path toward your destination in life. The Insight Lantern organizes these four main building blocks around the two polarities of a compass:

1. North to South – Intentions to Actions
We all have billions of intentions, but how many do we actually put into action? In this polarity you learn to notice and implement your intentions in order to generate more effective actions and create meaningful outcomes in your life.

2. East vs. West – Facts vs. Stories
We all create stories to make sense of life, but how many of us actually get clear on the facts to see where our stories might be off? In this polarity you learn to discern the objective facts from your subjective interpretations and stories, illuminating a clearer perspective to uncover what’s been blocking you on the path to success.

Using The Insight Lantern you’ll discover how naming and implementing your intentions in life naturally results in more effective behavior and actions, and how distinguishing the real facts from your interpretations of any situation can propel you toward radical clarity and true fulfillment.

BOLD DIALOGUES

The key benefit of using The Insight Lantern is that you’ll have more of what Gavin calls “Bold Dialogues.” Bold Dialogues are those that move you closer to what you’re wanting in life—the kind of human-to-human interactions that actually make a difference. By applying The Insight Lantern, you gain critical insight that opens your eyes to new opportunities for Bold Dialogues, helping you draw on your imagination and move beyond your current stance toward a positive outcome. Every conversation is a possibility waiting to be discovered. The more Bold Dialogues you have, the more profound and meaningful shifts you activate in your life.

PRACTICAL GUIDANCE

The book doesn’t just give you a theoretical understanding of how to gain more clarity in your life. Dr. Terlecki provides you with clear, practical steps to develop the core competencies you need to start getting the results you want. As you explore the book, you’ll find:

• A thorough description of all the directions of The Insight Lantern, each with three main points to focus your energy on.
• Case studies from Gavin’s many clients who have successfully used The Insight Lantern to transform their own lives.
• Hands-on practices Gavin has developed to help you put your new skills to use immediately.
• Step-by-step guidance to apply The Insight Lantern in any situation, including real-life stories from people who have experienced genuine transformation using this tool.

The Insight Lantern will help you to deepen your understanding of the challenges in your life, integrate new competencies to boost your effectiveness, and awaken to exciting opportunities for your own growth, leadership, and success!

ABOUT THE AUTHOR

Dr. Gavin Terlecki has over 30 years of experience with leadership development and executive coaching work. As owner and principal coach of Terlecki Growth Advisors, he has been integrating the fields of management consulting, business psychology, and leadership coaching since 1983. Gavin holds a Ph.D. in psychodynamic and group psychology from the Halvern Graduate Academy, an M.A. in human growth and potential from the Marlowe Ridge University, and a B.A. in accounting and Business Administration from Denby Valley University. He is the creator of The Insight Lantern™, a leadership development tool that supports people to see life clearly, wake up to exciting opportunities for their own growth and leadership, and take empowered action toward true success. Gavin’s combination of business expertise, human compassion, and incisive questions help his clients achieve unprecedented results.

Target Market(s)

Out intended audience is folks who would like to be more effective and to grow and transform. This being more productive and developing could be in their careers or their personal lives.

Industry/Entity Type

It Professional

Requirements
Must have
• Stock images, if used, that I can purchase exclusively or that you can easily create specifically for the book once you are the chosen designer. I completely understand using stock imaging in your submissions pre-selection.
Nice to have
• Ideally the cover will include both the title and subtitle.

```html
<!DOCTYPE html>
<html lang="en">
<head>
<meta charset="utf-8">
<title>The Insight Lantern – Book Cover Spread</title>
<link rel="stylesheet" href="https://fonts.googleapis.com/css2?family=Nunito+Sans:ital,wght@0,300;0,400;0,700;1,400&display=swap">
<style>
  :root {
    --stage: #000000;
    --paper: #ffffff;
    --slate-blue: #6b7ba3;
    --ink: #222222;
    --title-grey: #5b5b5b;
    --label-grey: #777777;
    --box-grey: #b3b3b3;
    --mist: #e3e6ef;
    --rule: #8a97b8;
  }
  * { margin: 0; padding: 0; box-sizing: border-box; }
  html, body { width: 1200px; height: 1000px; overflow: hidden; background: var(--stage); }
  body { font-family: "Nunito Sans", Arial, sans-serif; position: relative; }

  .spread { position: absolute; left: 124px; top: 153px; width: 957px; height: 695px; background: var(--paper); }

  /* Back cover */
  .back-cover { position: absolute; left: 0; top: 0; width: 457px; height: 695px; overflow: hidden; }
  .back-mark {
    position: absolute; left: 10px; top: 85px; width: 440px; height: 360px;
    background: radial-gradient(ellipse at 55% 50%, var(--mist) 0%, rgba(227,230,239,0.6) 45%, rgba(255,255,255,0) 70%);
  }
  .back-label { position: absolute; left: 33px; top: 49px; font-size: 11px; letter-spacing: 1.6px; color: var(--label-grey); }
  .back-rule { position: absolute; left: 33px; top: 74px; width: 394px; height: 1px; background: var(--rule); }
  .praise { position: absolute; left: 35px; top: 95px; width: 400px; font-size: 10.4px; line-height: 17px; color: var(--ink); }
  .praise-quote { margin: 0; }
  .praise-source { text-align: center; font-style: italic; color: var(--slate-blue); font-size: 10.4px; line-height: 12px; margin: 5px 0 8px 60px; }
  .praise-source .role { display: block; }
  .author-bio { position: absolute; left: 35px; top: 249px; width: 402px; font-size: 10.4px; line-height: 19px; color: var(--ink); }
  .author-photo { float: left; width: 64px; height: 83px; border: 2px solid var(--slate-blue); margin: 2px 6px 0 -1px; }
  .author-bio strong { color: var(--slate-blue); font-weight: 700; }
  .feature-note { position: absolute; top: 455px; width: 118px; font-size: 9.6px; line-height: 17px; color: var(--ink); }
  .feature-note.left { left: 80px; }
  .feature-note.right { left: 299px; }
  .series-mark { position: absolute; left: 190px; top: 448px; width: 102px; text-align: center; }
  .series-dot { display: block; width: 58px; height: 58px; border-radius: 50%; background: var(--slate-blue); margin: 0 auto 28px; }
  .series-name { font-size: 10.5px; line-height: 12px; color: var(--slate-blue); }
  .foot-rule { position: absolute; left: 33px; top: 581px; width: 394px; height: 1px; background: var(--rule); }
  .imprint-box {
    position: absolute; top: 603px; width: 112px; height: 58px; border: 1px solid var(--slate-blue);
    display: flex; align-items: center; justify-content: center;
    font-size: 11px; font-weight: 700; letter-spacing: 1px; color: var(--box-grey);
  }
  .imprint-box.publisher { left: 33px; }
  .imprint-box.upc { left: 317px; }

  /* Spine */
  .spine { position: absolute; left: 457px; top: 0; width: 43px; height: 695px; background: var(--slate-blue); color: var(--paper); }
  .spine-text { position: absolute; left: 0; width: 43px; writing-mode: vertical-rl; display: flex; align-items: center; font-size: 15px; letter-spacing: 1.4px; }
  .spine-title { top: 48px; }
  .spine-author { top: 492px; }

  /* Front cover */
  .front-cover { position: absolute; left: 500px; top: 0; width: 457px; height: 695px; }
  .front-author { position: absolute; left: 0; width: 457px; top: 38px; text-align: center; font-size: 22px; font-weight: 400; letter-spacing: 3.2px; color: var(--title-grey); }
  .front-rule { position: absolute; left: 0; top: 75px; width: 457px; height: 1px; background: var(--rule); }
  .front-title { position: absolute; left: 0; width: 457px; top: 80px; text-align: center; font-weight: 300; font-size: 70px; line-height: 66px; letter-spacing: -1px; }
  .front-title .line-one { display: block; color: var(--title-grey); }
  .front-title .line-two { display: block; color: var(--slate-blue); }
  .cover-emblem {
    position: absolute; left: 0; top: 190px; width: 480px; height: 385px;
    background: radial-gradient(ellipse at 48% 52%, var(--slate-blue) 0%, rgba(107,123,163,0.85) 38%, rgba(107,123,163,0) 68%);
  }
  .tagline { position: absolute; left: 0; top: 552px; font-size: 16.5px; letter-spacing: 2.6px; color: var(--ink); line-height: 32px; }
  .tagline span { display: block; white-space: nowrap; }
  .tagline .t1 { padding-left: 71px; }
  .tagline .t2 { padding-left: 45px; }
  .tagline .t3 { padding-left: 89px; }
</style>
</head>
<body>
  <div class="spread">
    <section class="back-cover">
      <div class="back-mark" role="img" aria-label="Faint Insight Lantern emblem as a background decoration"></div>
      <div class="back-label">LOREM IPSUM</div>
      <div class="back-rule"></div>
      <div class="praise">
        <p class="praise-quote">“Lorem ipsum greeking and more of the same this is praise for Dr. Terlecki’s new book lorem ipsum greeeking and you will see more clearly lorem ipsum.”</p>
        <p class="praise-source">- &nbsp;Harold Pemberton<span class="role">Director of Lorem Isum Center</span></p>
        <p class="praise-quote">“Lorem ipsum greeking and more of the same this is praise for Dr. Terlecki’s new book lorem ipsum greeking and you will see more clearly lorem ipsum.”</p>
        <p class="praise-source">- &nbsp;Lucinda Farraday<span class="role">Director of Lorem Isum Center</span></p>
      </div>
      <div class="author-bio">
        <div class="author-photo" role="img" aria-label="Author portrait placeholder"></div>
        <strong>Dr. Gavin Terlecki</strong> and more of the same this is praise for Dr. Terlecki’s new book lorem ipsum greeeking and you will see more clearly loremipsum . Lorem ipsum greeking and more of the same this is praise for Dr. Terlecki’s new book lorem ipsum greeeking and you will see more clearly lorem ipsum and more to see. Lorem ipsum greeking and more of the same this is praise for Dr. Terlecki’s new book lorem ipsum greeeking and you will see more clearly lorem ipsum plus newlor. Lorem ipsum greeking and more of the same this is praise for Dr. Terlecki’s new book lorem ipsum greeeking and you will see more clearly lorem ipsum .
      </div>
      <p class="feature-note left">Lorem ipsum greeking more of the same lorem greeking ipsum</p>
      <div class="series-mark">
        <span class="series-dot"></span>
        <span class="series-name">THE INSIGHT LANTERN</span>
      </div>
      <p class="feature-note right">Lorem ipsum greeking more of the same lorem greeking ipsum</p>
      <div class="foot-rule"></div>
      <div class="imprint-box publisher">PUBLISHER</div>
      <div class="imprint-box upc">UPC CODE</div>
    </section>

    <section class="spine">
      <div class="spine-text spine-title">THE INSIGHT LANTERN</div>
      <div class="spine-text spine-author">DR. GAVIN TERLECKI</div>
    </section>

    <section class="front-cover">
      <div class="front-author">DR. GAVIN TERLECKI</div>
      <div class="front-rule"></div>
      <h1 class="front-title"><span class="line-one">THE INSIGHT</span><span class="line-two">LANTERN</span></h1>
      <div class="cover-emblem" role="img" aria-label="Large Insight Lantern emblem, a slate blue compass star with ring"></div>
      <p class="tagline">
        <span class="t1">NOTICE EVERY SIGNAL.</span>
        <span class="t2">HOLD BOLD DIALOGUES.</span>
        <span class="t3">BUILD THE PATH YOU CHOOSE.</span>
      </p>
    </section>
  </div>
</body>
</html>
```